Bright Arc Electrical & Communications business card design

We would like a double sided business card that is different. Want it to be exciting and fun. Something that people keep rather then just throw it in the bin.
We have a logo that we want to put on one side of the business card and then the business information on the reverse side. Trying to go for a real professional style of business card

Target Market(s)

Electrical

Industry/Entity Type

Electrical

Contact Information for Business Card

Bright Arc Electrical & Communications
Marcus Trelowen
P: 0437 286 354
E: brightarc@mailrove.com.au
Lic No: 547106K
24/7

Font styles to use
Other font styles liked:
• Would like ideas

Requirements
Must have
• Our company logo (preferably on both sides) yellow needs to be incorporated somewhere. Business card card colours to match with logo. Maybe a small pop of colour
Nice to have
• Open to some design ideas

```html
<!DOCTYPE html>
<html lang="en">
<head>
<meta charset="utf-8">
<title>Bright Arc Electrical &amp; Communications – Business Card</title>
<link rel="stylesheet" href="https://fonts.googleapis.com/css2?family=Noto+Sans:wght@400;700&display=swap">
<style>
  :root {
    --backdrop: #2a2a2a;
    --card-grey: #7b7b7b;
    --card-grey-light: #8c8c8c;
    --card-white: #ffffff;
    --card-white-shade: #ececec;
    --accent-yellow: #f7e928;
    --line-yellow: #f2e35a;
    --ink-dark: #1c1c1c;
    --ink-body: #2b2b2b;
    --ink-light: #ffffff;
  }
  * { margin: 0; padding: 0; box-sizing: border-box; }
  html, body {
    width: 1200px; height: 900px; overflow: hidden;
    background: var(--backdrop);
    font-family: "Noto Sans", sans-serif;
  }
  .canvas {
    width: 1200px; height: 900px;
    display: flex; flex-direction: column; align-items: center; justify-content: center;
    gap: 56px;
  }
  .card {
    position: relative;
    width: 620px; height: 360px;
    border-radius: 22px;
    overflow: hidden;
  }

  /* Front side */
  .card--front {
    background: linear-gradient(160deg, var(--card-grey-light), var(--card-grey));
  }
  .front-brand {
    position: absolute; left: 0; right: 0; top: 70px;
    display: flex; align-items: center; justify-content: center; gap: 14px;
  }
  .brand-mark {
    width: 26px; height: 26px; background: var(--accent-yellow);
  }
  .brand-name {
    font-weight: 700; font-size: 25px; line-height: 1.15;
    letter-spacing: 1px; text-transform: uppercase;
  }
  .front-brand .brand-name { color: var(--ink-light); }
  .service-band {
    position: absolute; left: 0; right: 0; top: 232px; height: 62px;
    background: var(--accent-yellow);
    display: flex; align-items: center; justify-content: flex-end;
    padding-right: 70px;
  }
  .service-band__text {
    font-size: 19px; color: var(--ink-body);
  }

  /* Back side */
  .card--back {
    background: linear-gradient(135deg, var(--card-white) 40%, var(--card-white-shade));
  }
  .back-brand {
    position: absolute; right: 40px; top: 46px;
    display: flex; align-items: center; gap: 14px;
  }
  .back-brand .brand-name { color: var(--ink-dark); font-size: 23px; }
  .licence {
    position: absolute; right: 34px; top: 188px;
    font-size: 19px; color: var(--ink-body);
  }
  .contact {
    position: absolute; left: 30px; bottom: 26px; width: 440px;
  }
  .contact__role {
    display: block; text-align: right;
    font-size: 13px; color: var(--ink-body); margin-bottom: 4px;
  }
  .contact__name {
    font-size: 22px; color: var(--ink-body);
    padding-bottom: 6px;
    border-bottom: 2px solid var(--line-yellow);
    margin-bottom: 12px;
  }
  .contact__row {
    display: flex; align-items: center; gap: 12px;
    font-size: 16px; color: var(--ink-body); margin-top: 6px;
  }
  .contact__icon { width: 20px; height: 20px; flex: none; }
</style>
</head>
<body>
<main class="canvas">

  <section class="card card--front" aria-label="Business card front">
    <div class="front-brand">
      <span class="brand-mark"></span>
      <span class="brand-name">Bright Arc Electrical<br>&amp; Communications</span>
    </div>
    <div class="service-band">
      <span class="service-band__text">Service Available 24/7</span>
    </div>
  </section>

  <section class="card card--back" aria-label="Business card back">
    <div class="back-brand">
      <span class="brand-mark"></span>
      <span class="brand-name">Bright Arc Electrical<br>&amp; Communications</span>
    </div>

    <p class="licence">Licence No: 547106K</p>

    <div class="contact">
      <span class="contact__role">Owner</span>
      <p class="contact__name">Marcus Trelowen</p>
      <p class="contact__row">
        <svg class="contact__icon" viewBox="0 0 20 20" aria-hidden="true">
          <circle cx="10" cy="10" r="8.5" fill="none" stroke="#f2e35a" stroke-width="1.6"/>
          <path d="M7 5.5 L8.6 5.5 L9.3 8 L8.2 8.8 Q9.2 11 11.2 11.8 L12 10.7 L14.5 11.4 L14.5 13 Q13 14.6 10 13 Q7 11 6 8 Q5.7 6.4 7 5.5 Z" fill="#f2e35a"/>
        </svg>
        0437 286 354
      </p>
      <p class="contact__row">
        <svg class="contact__icon" viewBox="0 0 20 20" aria-hidden="true">
          <rect x="2" y="4.5" width="16" height="11" fill="none" stroke="#f2e35a" stroke-width="1.6"/>
          <path d="M2 4.5 L10 11 L18 4.5" fill="none" stroke="#f2e35a" stroke-width="1.6"/>
        </svg>
        brightarc@mailrove.com.au
      </p>
    </div>
  </section>

</main>
</body>
</html>
```